Logo and Double sided business card

We need a logo and business card for a Point of Sale Business, Website is www.kestreltill.com.au - this is being worked on at the moment. There is a logo on the website - but this is more of a placement /logo and needs to be redesigned.
The address for Details for the Business card are

Person Name
KESTREL TILL
17/3 Worrigal Pde
Brindale Vale 2167
Ph 1300 585 926 (1300 KTL 926)
Email : Person@kestreltill.com.au
Web: www.kestreltill.com.au

Our company will be a Point of Sale installation and Support business. We Specialise in the Vandrel Quill system.

We do
Installation of POS Systems
Support and Maintenance of existing POS
Quill POS support
Updates

Target Market(s)

Restaurants, hotels, retail shops

Industry/Entity Type

Business

Contact Information for Business Card

Person Name
KESTREL TILL
17/3 Worrigal Pde
Brindale Vale 2167
Web: www.kestreltill.com.au

Logo Text

Kestrel Till

Font styles to use
Serif

Requirements
Must have
• We must have the source graphics in editable formats for both logo and business card.

```html
<!DOCTYPE html>
<html lang="en">
<head>
<meta charset="utf-8">
<title>Kestrel Till – Business Card</title>
<link href="https://fonts.googleapis.com/css2?family=Montserrat:wght@400;500;700;800&display=swap" rel="stylesheet">
<style>
  :root {
    --yellow: #ffc914;
    --ink: #111213;
    --paper: #ffffff;
    --backdrop: #ececea;
    --text-grey: #4a4a4a;
    --rule: #f2b705;
  }
  * { box-sizing: border-box; margin: 0; padding: 0; }
  html, body { width: 1200px; height: 1000px; overflow: hidden; }
  body {
    background: var(--backdrop);
    font-family: "Montserrat", sans-serif;
    position: relative;
  }
  .card {
    position: absolute;
    width: 600px;
    height: 350px;
    left: 300px;
    overflow: hidden;
    box-shadow: 0 6px 18px rgba(0,0,0,0.18);
  }
  /* Front side */
  .card-front { top: 90px; background: var(--paper); }
  .brand-front {
    position: absolute;
    left: 48px;
    top: 124px;
    display: flex;
    align-items: center;
    gap: 10px;
  }
  .brand-square { width: 18px; height: 18px; background: var(--yellow); }
  .brand-name {
    font-weight: 800;
    font-size: 19px;
    letter-spacing: 0.3px;
    color: var(--ink);
    white-space: nowrap;
  }
  .divider {
    position: absolute;
    left: 262px;
    top: 62px;
    width: 1.5px;
    height: 120px;
    background: var(--rule);
  }
  .contact { position: absolute; left: 284px; top: 58px; color: var(--text-grey); }
  .contact-name { font-weight: 700; font-size: 23px; color: var(--ink); margin-bottom: 6px; }
  .contact-phone { font-size: 13.5px; margin-bottom: 14px; }
  .contact-line { font-size: 13.5px; line-height: 1.3; white-space: nowrap; }

  .service {
    position: absolute;
    width: 200px;
    display: flex;
    align-items: center;
    justify-content: center;
    text-align: center;
    font-size: 12px;
    line-height: 1.25;
    padding: 0 34px;
  }
  .service::before {
    content: "";
    position: absolute;
    top: -8px;
    width: 0; height: 0;
    border-left: 8px solid transparent;
    border-right: 8px solid transparent;
    border-bottom: 8px solid currentColor;
  }
  .service-dark { background: var(--ink); color: var(--paper); }
  .service-dark::before { border-bottom-color: var(--ink); }
  .service-light { background: var(--yellow); color: var(--ink); }
  .service-light::before { border-bottom-color: var(--yellow); }
  .service-install { left: 0; top: 268px; height: 62px; }
  .service-install::before { left: 130px; }
  .service-quill { left: 200px; top: 248px; height: 62px; }
  .service-quill::before { left: 70px; }
  .service-maintain { left: 400px; top: 222px; height: 66px; padding: 0 40px; }
  .service-maintain::before { left: 160px; }

  /* Back side */
  .card-back { top: 520px; background: var(--paper); padding: 18px; }
  .back-field {
    width: 100%;
    height: 100%;
    background: var(--yellow);
    display: flex;
    align-items: center;
    justify-content: center;
    gap: 16px;
  }
  .brand-back-square { width: 34px; height: 34px; background: var(--ink); }
  .brand-back-name {
    font-weight: 800;
    font-size: 44px;
    letter-spacing: 1px;
    color: var(--ink);
  }
</style>
</head>
<body>
  <section class="card card-front" aria-label="Business card front">
    <div class="brand-front">
      <span class="brand-square"></span>
      <span class="brand-name">KESTREL TILL</span>
    </div>
    <div class="divider"></div>
    <div class="contact">
      <p class="contact-name">John Doe</p>
      <p class="contact-phone">1300 585 926 (1300 KTL 926)</p>
      <p class="contact-line">Person@kestreltill.com.au</p>
      <p class="contact-line">www.kestreltill.com.au</p>
      <p class="contact-line">17/3 Worrigal Pde, Brindale Vale 2167</p>
    </div>
    <div class="service service-dark service-install">Installation of POS Systems</div>
    <div class="service service-light service-quill">Quill POS support</div>
    <div class="service service-dark service-maintain">Support and Maintenance of existing POS</div>
  </section>

  <section class="card card-back" aria-label="Business card back">
    <div class="back-field">
      <span class="brand-back-square"></span>
      <span class="brand-back-name">KESTREL TILL</span>
    </div>
  </section>
</body>
</html>
```